****FLYER design - LAW FIRM ADVERTISEMENT****

We are a small law firm based in Los Angeles, CA. We need an flyer used for advertising that we will be passing out. We want the flyer to be about 4in x 6in.

We want the flyer to advertise the name of our firm: MORVANTE KELDRIC LLP (no period)
- We want our group photo to take up a good portion of the flyer (although it's okay if parts of the photo have wording over it.)

COLORS: Our firm colors are different shades of steal/metal grey with a bit of a bold orange accent. Any bold writing, like our slogan, names of practice areas,... should be in orange.

We envision a horizontal lay-out of the flyer, but are open to creative options laid out vertically!

Feel free to play with the fonts, the sizing, the color combinations,...

We want the flyer to advertise our two areas of practice: PERSONAL INJURY and EMPLOYMENT LAW. Please also place each photo icon of our areas of practice somewhere around the name (ambulance photo for personal injury; person behind computer desk for employment law). The icons can be relatively small.

Under Personal Injury, please write:
If you or a loved one are suffering from an injury or wrongful death caused by the careless or intentional acts of others, then you have the right to pursue compensation for your injury, out-of-pocket expenses, lost wages, emotional anguish, and more.

Under Employment Law, please write:
Our attorneys regularly represent clients in disputes involving sex, age and race discrimination, sexual harassment, retaliatory discharge, defamation, unlawful termination, breach of employment contracts, and more.

Somewhere on the flyer, please write our slogan IN ITALICS (and probably in orange):
- You Speak. We Listen. They Pay.

In somewhat bright and bold writing, please write "CONTACT US FOR A FREE CONSULTATION TODAY!" (maybe just after our slogan?)
- And under that phrase, write:
- 731 W. Larkmoor Avenue, Suite 400 Glenfield, CA 90488
phone: 555.318.9062
fax: 555.318.9074
email: info@mkrlegal-example.com
web: www.mkrlegal-example.com

If possible, and only if there's room without it looking too busy, somewhere in the upper left corner, place our "MKR" logo.
Updates

PLEASE NOTE THAT WE CHANGED OUR GROUP PHOTO TO A SLIGHTLY EDITED ONE.  PLEASE BE SURE TO USE THE NEW ONE!!!  (We deleted the old.)

Target Market(s)

employees, lower and mid-income individuals, minority communities. However, we still want the flyer to look sleek, modern, and professional.

Industry/Entity Type

Advertising

Requirements
Must have
• Firm Name,
Photo of Partners,
Names, photos, and small description of practice areas,
Firm slogan,
"Contact us for a free consultation today!",
Firm contact info.

And only if space and overall look permits, firm "MKR" logo.

We want an overall very sleek, modern feel to our flyer. While we do want to look professional, we wanted a more approachable feel than the typical, conservative law offices.
Nice to have
• Firm "MKR" logo

Horizontal lay out, though we're open to vertical options.

```html
<!DOCTYPE html>
<html lang="en">
<head>
<meta charset="utf-8">
<title>Morvante Keldric LLP – Flyer</title>
<link rel="stylesheet" href="https://fonts.googleapis.com/css2?family=Oswald:wght@500;600;700&family=Open+Sans:wght@400;700&display=swap">
<style>
  :root{
    --orange:#e0661a;
    --orange-dark:#c4530f;
    --steel-dark:#1f2a33;
    --steel:#6e7680;
    --steel-light:#b9bec4;
    --paper:#f2f2f2;
    --ink:#111111;
    --body-text:#55595e;
    --stage:#e6e6e6;
    --white:#ffffff;
  }
  *{margin:0;padding:0;box-sizing:border-box}
  html,body{width:1200px;height:936px;overflow:hidden;background:var(--stage)}
  .flyer{position:absolute;left:60px;top:108px;width:1080px;height:720px;background:linear-gradient(180deg,var(--white) 0%,var(--paper) 100%);overflow:hidden;box-shadow:0 6px 24px rgba(0,0,0,.18)}
  .flyer-shapes{position:absolute;inset:0}
  .firm-name{position:absolute;left:0;top:16px;width:440px;text-align:center;font-family:"Oswald",sans-serif;font-weight:700;font-size:82px;line-height:90px;color:var(--white);letter-spacing:1px}
  .practice{position:absolute;left:15px;width:600px}
  .practice--injury{top:248px}
  .practice--employment{top:394px}
  .practice-icon{position:absolute;left:0;top:0;width:103px;height:103px;background:var(--steel-dark)}
  .practice-title{position:absolute;left:110px;top:-4px;font-family:"Open Sans",sans-serif;font-weight:700;font-size:22px;color:var(--orange)}
  .practice-text{position:absolute;left:111px;top:28px;font-family:"Open Sans",sans-serif;font-size:13.5px;line-height:19px;color:var(--body-text)}
  .practice--injury .practice-text{width:345px}
  .practice--employment .practice-text{width:420px}
  .slogan{position:absolute;left:0;top:516px;width:1080px;text-align:center;font-family:"Oswald",sans-serif;font-weight:600;font-size:56px;line-height:70px;color:var(--ink);letter-spacing:.5px}
  .contact-band{position:absolute;left:0;top:595px;width:1080px;height:125px;background:linear-gradient(180deg,var(--orange) 0%,var(--orange-dark) 100%)}
  .firm-mark{position:absolute;left:17px;top:585px;width:103px;height:100px;background:var(--steel);display:flex;align-items:center;justify-content:center;font-family:"Oswald",sans-serif;font-weight:500;font-size:30px;letter-spacing:6px;color:var(--white)}
  .contact-heading{position:absolute;left:198px;top:600px;font-family:"Oswald",sans-serif;font-weight:600;font-size:30px;line-height:40px;color:var(--white)}
  .contact-col{position:absolute;top:646px;font-family:"Open Sans",sans-serif;font-size:15px;line-height:24px;color:var(--white);font-style:normal;white-space:nowrap}
  .contact-col--address{left:198px}
  .contact-col--reach{left:505px}
  .contact-col--web{left:800px}
</style>
</head>
<body>
<main class="flyer">
  <svg class="flyer-shapes" width="1080" height="720" viewBox="0 0 1080 720">
    <defs>
      <linearGradient id="headerFill" x1="0" y1="0" x2="0" y2="1">
        <stop offset="0" stop-color="#e87024"/>
        <stop offset="1" stop-color="#c9560f"/>
      </linearGradient>
      <linearGradient id="photoTone" x1="0" y1="0" x2="1" y2="1">
        <stop offset="0" stop-color="#6b5a44"/>
        <stop offset=".45" stop-color="#3a3430"/>
        <stop offset="1" stop-color="#d9d4cc"/>
      </linearGradient>
    </defs>
    <rect class="header-band" x="0" y="0" width="520" height="210" fill="url(#headerFill)"/>
    <path class="photo-ring" d="M430,0 H1080 V490 C900,520 730,520 620,455 C500,380 440,210 430,0 Z" fill="#c5c8cc"/>
    <path class="group-photo" role="img" aria-label="Group photo of the firm's three partners" d="M446,0 H1080 V476 C900,506 736,504 632,443 C516,372 456,206 446,0 Z" fill="url(#photoTone)"/>
  </svg>

  <h1 class="firm-name">MORVANTE<br>KELDRIC</h1>

  <section class="practice practice--injury">
    <svg class="practice-icon" viewBox="0 0 103 103" aria-label="Ambulance icon" role="img">
      <rect width="103" height="103" fill="#1f2a33"/>
      <path d="M18,38 H62 V70 H18 Z M62,46 H76 L86,58 V70 H62 Z" fill="#fff"/>
      <rect x="66" y="50" width="10" height="8" fill="#1f2a33"/>
      <rect x="36" y="44" width="8" height="20" fill="#1f2a33"/>
      <rect x="30" y="50" width="20" height="8" fill="#1f2a33"/>
      <circle cx="32" cy="72" r="7" fill="#fff" stroke="#1f2a33" stroke-width="3"/>
      <circle cx="74" cy="72" r="7" fill="#fff" stroke="#1f2a33" stroke-width="3"/>
    </svg>
    <h2 class="practice-title">Personal Injury</h2>
    <p class="practice-text">If you or a loved one are suffering from an injury or wrongful death caused by the careless or intentional acts of others, then you have the right to pursue compensation for your injury, out-of-pocket expenses, lost wages, emotional anguish, and more.</p>
  </section>

  <section class="practice practice--employment">
    <svg class="practice-icon" viewBox="0 0 103 103" aria-label="Person at computer desk icon" role="img">
      <rect width="103" height="103" fill="#1f2a33"/>
      <circle cx="36" cy="26" r="7" fill="#fff"/>
      <path d="M30,36 H42 L46,56 H56 V62 H38 L30,44 Z" fill="#fff"/>
      <path d="M38,62 H44 V80 H38 Z M28,60 H34 V80 H28 Z" fill="#fff"/>
      <rect x="50" y="52" width="38" height="5" fill="#fff"/>
      <rect x="82" y="57" width="4" height="25" fill="#fff"/>
      <rect x="58" y="34" width="20" height="15" fill="#fff"/>
      <rect x="66" y="49" width="4" height="3" fill="#fff"/>
    </svg>
    <h2 class="practice-title">Employment Law</h2>
    <p class="practice-text">Our attorneys regularly represent clients in disputes involving sex, age and race discrimination, sexual harassment, retaliatory discharge, defamation, unlawful termination, breach of employment contracts, and more.</p>
  </section>

  <p class="slogan">YOU SPEAK. WE LISTEN. THEY PAY.</p>

  <footer class="contact-band"></footer>
  <div class="firm-mark">MKR</div>
  <p class="contact-heading">CONTACT US FOR A FREE CONSULTATION TODAY!</p>
  <address class="contact-col contact-col--address">731 W. Larkmoor Avenue,<br>Suite 400 Glenfield, CA 90488</address>
  <p class="contact-col contact-col--reach">Phone: 555.318.9062<br>Email: info@mkrlegal-example.com</p>
  <p class="contact-col contact-col--web">Fax: 555.318.9074<br>Web: www.mkrlegal-example.com</p>
</main>
</body>
</html>
```